January 2013 Flyer

Hi,

Flyer for a winter flooring sale.
Warm and cozy look.
It should be professional, clean, not cluttered. Nice color.

Our clients have expensive homes in a modern west coast contemporary design. Clean lines and colours.

The flyer should represent that style.

Target Market(s)

Mid to High income house owners
30-65yrs old.
Often baby boomers whose kids have left and finally can renovate the way they've always wanted.

Industry/Entity Type

Flooring

Requirements
Must have
• 1) The Larkfield Surfaces logo and contact info.
2) It must have the at least one of the Dovetrail logo provided, displayed in the carpet sale section.
3) WRSGU, PKTO, and QHM logos

www.larkfieldsurfaces.example

As well as QHM, PKTO, as well as Pinecrest Floor covering association logo.

Specials on Dovetrail Carpet:
Multicolor Berber Carpet - 2 Styles, 24 colors
$2.39 $ 1.59

35oz Plush Vomarel Carpet - 2 Styles, 30 Colors $2.89 $ 1.99

Patterned Vomarel Carpet, 12 Colors
$2.99 $ 1.99

50oz Freize Vomarel Carpet, 2 Styles - 28 Colors $2.99 $ 2.39

Gleamhold Berber Carpet - 12 Colors
$3.59 $ 2.39

5” Designer engineered hardwood - 10 different styles
$6.25 $4.99

12” X 36” Swiss-made Commercial-grade vinyl cork planking
$6.75 $3.99

I have more files but its too big to put on here such as: room scenes
Nice to have
• Our clients have homes in a modern west coast contemporary design. Clean lines and colours.

Should not have
• I don't want an old simple flyer. Colours shouldn't be boring,

```html
<!DOCTYPE html>
<html lang="en">
<head>
<meta charset="utf-8">
<title>Larkfield Surfaces – Winter Carpet Sale</title>
<link rel="stylesheet" href="https://fonts.googleapis.com/css2?family=Open+Sans:wght@300;400;600;700;800&display=swap">
<style>
  :root {
    --stage: #2b2b2d;
    --navy: #1f2a7a;
    --red: #e3222b;
    --ink: #222226;
    --muted: #5a5a60;
    --card-top: #ffffff;
    --card-bottom: #b9b9bd;
    --footer: #8e8e93;
    --white: #ffffff;
  }
  * { box-sizing: border-box; margin: 0; padding: 0; }
  html, body { width: 1200px; height: 793px; overflow: hidden; }
  body {
    background: var(--stage);
    font-family: "Open Sans", sans-serif;
    position: relative;
  }

  /* ---------- price list card ---------- */
  .price-card {
    position: absolute; left: 210px; top: 68px;
    width: 352px; height: 642px;
    background: linear-gradient(180deg, var(--card-top) 0%, #e2e2e5 35%, var(--card-bottom) 100%);
    box-shadow: 0 6px 18px rgba(0,0,0,.5);
    overflow: hidden;
  }
  .brand {
    display: flex; align-items: center; gap: 8px;
    color: var(--navy); font-weight: 400; letter-spacing: 3px;
  }
  .brand-mark { width: 12px; height: 12px; background: var(--red); }
  .price-card .brand {
    position: absolute; left: 20px; top: 12px; font-size: 21px;
  }
  .header-rule {
    position: absolute; left: 60px; right: 14px; top: 46px;
    height: 2px; background: var(--navy);
  }
  .feature-names {
    position: absolute; left: 28px; top: 88px;
    font-size: 13px; line-height: 21px; color: var(--ink); text-transform: uppercase;
  }
  .feature-names .or { text-transform: none; }
  .big-price {
    position: absolute; right: 34px; top: 54px;
    color: var(--red); font-weight: 600; line-height: 1;
    text-shadow: 2px 2px 0 var(--white), 4px 4px 6px rgba(0,0,0,.35);
    display: flex; align-items: flex-start;
  }
  .big-price .cur { font-size: 40px; margin-top: 38px; }
  .big-price .whole { font-size: 78px; letter-spacing: -2px; }
  .big-price .frac { display: flex; flex-direction: column; align-items: center; margin-left: 2px; }
  .big-price .cents { font-size: 42px; margin-top: 4px; }
  .big-price .unit { font-size: 22px; margin-top: 2px; }

  .price-list {
    position: absolute; left: 30px; right: 30px; top: 158px;
    list-style: none;
  }
  .price-list li {
    display: flex; justify-content: space-between; align-items: flex-end;
    height: 26px; padding-bottom: 2px;
    border-bottom: 1px dashed #55555b;
    font-size: 12px; color: var(--ink);
  }
  .price-list .amt { font-size: 12px; }
  .price-list .amt b { font-weight: 700; }

  .partner-strip {
    position: absolute; left: 46px; right: 26px; top: 470px; height: 76px;
    background: var(--white);
    display: flex; align-items: center; justify-content: space-around; padding: 0 10px;
  }
  .badge-tall { width: 20px; height: 46px; background: #24408e; }
  .badge-wide { width: 72px; height: 14px; background: #2b8ccc; border-radius: 7px; }
  .badge-round { width: 22px; height: 22px; border-radius: 50%; background: #333; }
  .badge-rect { width: 62px; height: 18px; background: #9ccc7a; }
  .partner-name { font-size: 7px; color: var(--ink); max-width: 64px; line-height: 1.2; }

  .contacts-title {
    position: absolute; left: 0; right: 0; top: 548px; text-align: center;
    font-size: 38px; font-weight: 300; color: #a9a9ae; letter-spacing: 1px;
  }
  .contact-footer {
    position: absolute; left: 0; right: 0; bottom: 0; height: 70px;
    background: var(--footer);
    color: var(--white); font-size: 8px; line-height: 12px; text-align: center;
    padding: 14px 0 0 100px;
  }

  /* ---------- sale card ---------- */
  .sale-card {
    position: absolute; left: 630px; top: 70px;
    width: 326px; height: 648px;
    box-shadow: 0 6px 18px rgba(0,0,0,.5);
    overflow: hidden;
  }
  .room-photo {
    position: absolute; inset: 0;
    background: linear-gradient(180deg, #f6f6f6 0%, #e9ecec 35%, #d7d9d6 52%, #b9a98f 70%, #8f7a5e 86%, #6e5c45 100%);
  }
  .sale-card .brand {
    position: absolute; left: 24px; top: 50px; font-size: 21px;
  }
  .sale-banner {
    position: absolute; left: 38px; top: 142px; width: 252px; height: 110px;
    background: var(--red); color: var(--white);
    transform: rotate(-2deg);
    text-align: right; padding: 10px 16px 0 0; line-height: 1;
  }
  .sale-banner .line1 { font-size: 28px; font-weight: 400; }
  .sale-banner .line1 b { font-weight: 800; }
  .sale-banner .line2 { font-size: 58px; font-weight: 800; margin-top: 2px; }
  .from-price {
    position: absolute; left: 68px; top: 540px;
    color: var(--white); display: flex; align-items: flex-end; line-height: 1;
  }
  .from-price .lead { font-size: 19px; margin-right: 8px; margin-bottom: 8px; }
  .from-price .cur { font-size: 30px; margin-bottom: 4px; }
  .from-price .whole { font-size: 54px; }
  .from-price .frac { display: flex; flex-direction: column; margin-left: 2px; margin-bottom: 6px; }
  .from-price .cents { font-size: 28px; }
  .from-price .unit { font-size: 14px; }
  .web-band {
    position: absolute; left: 0; right: 0; bottom: 0; height: 26px;
    background: var(--red); color: var(--white);
    font-size: 13px; text-align: center; line-height: 26px;
  }
</style>
</head>
<body>

<section class="price-card">
  <div class="brand"><span class="brand-mark"></span><span>larkfieldsurfaces</span></div>
  <div class="header-rule"></div>

  <div class="feature-names">Marshwren<br><span class="or">or</span><br>Tidegull</div>
  <div class="big-price">
    <span class="cur">$</span><span class="whole">1</span>
    <span class="frac"><span class="cents">59</span><span class="unit">sq ft</span></span>
  </div>

  <ul class="price-list">
    <li><span>Stillbrook I &amp; II:</span><span class="amt"><b>$1.99</b>/sqft</span></li>
    <li><span>Slow Harbour:</span><span class="amt"><b>$1.99</b>/sqft</span></li>
    <li><span>Ashgrove Living:</span><span class="amt"><b>$1.99</b>/sqft</span></li>
    <li><span>Bright Hour:</span><span class="amt"><b>$2.39</b>/sqft</span></li>
    <li><span>Vellor:</span><span class="amt"><b>$2.39</b>/sqft</span></li>
    <li><span>Sunward:</span><span class="amt"><b>$2.59</b>/sqft</span></li>
    <li><span>Lagoon Lane:</span><span class="amt"><b>$2.69</b>/sqft</span></li>
    <li><span>Seawall Row:</span><span class="amt"><b>$2.89</b>/sqft</span></li>
    <li><span>Merrymark:</span><span class="amt"><b>$2.89</b>/sqft</span></li>
    <li><span>Quiet Charm:</span><span class="amt"><b>$3.19</b>/sqft</span></li>
    <li><span>Highcrest:</span><span class="amt"><b>$3.29</b>/sqft</span></li>
    <li><span>Old Crownley:</span><span class="amt"><b>$3.99</b>/sqft</span></li>
  </ul>

  <div class="partner-strip">
    <span class="badge-tall" aria-label="QHM badge"></span>
    <span class="partner-name">DOVETRAIL</span>
    <span class="badge-round" aria-label="PKTO badge"></span>
    <span class="partner-name">PKTO</span>
    <span class="badge-rect" aria-label="Pinecrest Floor covering association badge"></span>
  </div>

  <div class="contacts-title">CONTACTS</div>
  <div class="contact-footer">
    2240 Harrow Lane, Eastbrook, V9K 4T2<br>
    Phone: 000 555 0142 &nbsp; Fax: 000 555 0187<br>
    contact@larkfieldsurfaces.example<br>
    www.larkfieldsurfaces.example
  </div>
</section>

<section class="sale-card">
  <div class="room-photo" role="img" aria-label="Bright modern living room with white sofas, orange cushions and a shaggy beige carpet"></div>
  <div class="brand"><span class="brand-mark"></span><span>larkfieldsurfaces</span></div>
  <div class="sale-banner">
    <div class="line1"><b>WINTER</b> CARPET</div>
    <div class="line2">SALE</div>
  </div>
  <div class="from-price">
    <span class="lead">prices from</span>
    <span class="cur">$</span><span class="whole">1</span>
    <span class="frac"><span class="cents">59</span><span class="unit">sq ft</span></span>
  </div>
  <div class="web-band">www.larkfieldsurfaces.example</div>
</section>

</body>
</html>
```